New Wordpress Design Project: KV- Kindred Vantage, Training Beyond Equity, Diversity, and Inclusion

I need a clean, modern, website design for KV- a national consulting firm providing equity, diversity, and inclusion training, through the lens of undoing racism, for arts and culture, and the non profit industry. It will feature both written posts, and some video. People will need KV contact information, and subscribe to receive information. It will feature a pretty active blog, and a section for resources, with links to other sites. There needs to be a section about KV,its training, approach, and bio Information. I probably should have put this first!

I want a site that draws people in. That is interesting and dynamic. My approach to this work is to provide people with the information, knowledge, and tools they need to go back to their communities and do the work. So they are at the center of the story. And I like powerful imagery. It could also be pretty.

The idea of undoing racism is a big idea. It is powerful, heroic even. And thousands of people in the US are working hard to do just that. So there is a sense of movement building here, of connecting to something important.

I already have a logo design that was done through a contest here last month.

Target Market(s)

Arts and culture fields, non profit industry, and philanthropy

Font styles to use
Sans Serif

Requirements
Must have
• Must have dynamic powerful imagery, be clean and easy to navigate, support concept of story telling, good use of color, be inviting, draw people in to learn when they see it first time. The ability to update photos, and videos easily. Connect to social media, especially Facebook and LinkedIn.
Nice to have
• It would be nice to have a website that uses more images than words to tell stories. I don't know enough about what's possible in website design to add more to this section.
Should not have
• Should not look like we are selling products, or services even but, rather, providing essential information and knowledge to help people make this world a better place for more people.

```html
<!DOCTYPE html>
<html lang="en">
<head>
<meta charset="utf-8">
<title>Kindred Vantage</title>
<link href="https://fonts.googleapis.com/css2?family=Roboto:wght@300;400;500;700&family=Lora:ital@1&display=swap" rel="stylesheet">
<style>
:root{
  --black:#000;
  --yellow:#ffd800;
  --band:#ffe100;
  --ink:#444;
  --heading:#3a3a3a;
  --muted:#8a8a8a;
  --soft:#f4f5f7;
  --line:#d9d9d9;
  --white:#fff;
  --dark-btn:#4a4a4a;
}
*{margin:0;padding:0;box-sizing:border-box}
html,body{width:1200px;height:2564px;overflow:hidden}
body{position:relative;background:var(--white);font-family:'Roboto',Arial,sans-serif;color:var(--ink)}
.abs{position:absolute}
.center{text-align:center}

/* header */
.site-header{left:0;top:0;width:1200px;height:86px;background:var(--black);border-bottom:4px solid var(--yellow)}
.brand{left:78px;top:22px;display:flex;align-items:center;gap:10px}
.brand-dot{width:38px;height:38px;border:3px solid var(--yellow);border-radius:50%}
.brand-name{color:var(--white);font-size:17px;font-weight:400}
.main-nav a{position:absolute;top:36px;color:var(--white);font-size:12px;font-weight:500;text-decoration:none;letter-spacing:.2px;transform:translateX(-50%)}
.main-nav a.active{color:var(--yellow)}
.search-btn{left:1067px;top:20px;width:46px;height:46px;border:2px solid var(--yellow);border-radius:50%}

/* hero */
.hero{left:0;top:90px;width:1200px;height:484px;background:var(--white);border-bottom:1px solid var(--line)}
.hero-photo{left:197px;top:0;width:803px;height:484px;background:linear-gradient(90deg,#e9c9a0 0%,#f2f0ec 35%,#f7f7f5 55%,#e6e2d6 80%,#f0eee9 100%)}
.hero-arrow{top:214px;width:54px;height:54px;border:2px solid #bbb;border-radius:50%;background:rgba(255,255,255,.6)}

/* section heads */
.section-title{width:1200px;left:0;font-size:22px;font-weight:400;color:var(--heading);letter-spacing:.5px}
.section-sub{width:1200px;left:0;font-size:11px;color:var(--muted)}

/* services */
.service{width:300px;text-align:center}
.service-icon{margin:0 auto;width:112px;height:112px;border-radius:50%;border:3px solid #4d4d4d;padding:4px}
.service-icon .inner{width:100%;height:100%;border-radius:50%;background:#575757;display:flex;align-items:center;justify-content:center}
.service-icon.accent{border-color:#4d4d4d}
.service-icon.accent .inner{background:var(--yellow)}
.service h3{margin-top:19px;font-size:17px;font-weight:400;color:var(--heading);letter-spacing:.5px}
.service p{margin-top:12px;font-size:11px;line-height:24px;color:var(--muted)}

/* welcome */
.welcome{left:0;top:969px;width:1200px;height:415px;background:var(--soft)}
.welcome h2{left:87px;top:40px;font-size:22px;font-weight:400;color:var(--heading)}
.welcome .tagline{left:87px;top:82px;font-size:13px;font-weight:700;color:var(--yellow)}
.welcome p{left:87px;width:440px;font-size:11.5px;line-height:24px;color:var(--muted)}
.btn-outline{left:87px;top:331px;width:137px;height:38px;border:1px solid #bdbdbd;border-radius:3px;font-size:12px;color:#666;display:flex;align-items:center;justify-content:center}
.video{left:581px;top:44px;width:532px;height:328px;background:linear-gradient(90deg,#c7392e 0%,#8e8c89 35%,#b8b8b6 60%,#6e6e6e 100%)}
.play{left:230px;top:128px;width:72px;height:72px;border:3px solid var(--white);border-radius:50%}

/* blog */
.post{top:1506px;width:330px}
.post-img{height:205px}
.post h3{margin-top:33px;font-size:16px;font-weight:500;color:var(--heading)}
.post p{margin-top:16px;font-size:11px;line-height:24px;color:var(--muted)}
.post-meta{margin-top:16px;height:40px;border-top:1px solid var(--line);border-bottom:1px solid var(--line);display:flex;align-items:center;gap:34px;padding-left:8px;font-family:'Lora',serif;font-style:italic;font-size:12px;color:var(--muted)}
.post-meta span{display:flex;align-items:center;gap:6px}

/* newsletter */
.newsletter{left:0;top:1965px;width:1200px;height:88px;background:var(--band)}
.newsletter .label{left:248px;top:32px;color:var(--white);font-size:20px;font-weight:500;letter-spacing:.5px}
.newsletter .field{left:526px;top:25px;width:358px;height:38px;border-radius:19px;background:var(--white);font-size:11px;color:#555;padding-left:20px;display:flex;align-items:center}
.newsletter .submit{left:902px;top:25px;width:151px;height:38px;border-radius:19px;background:var(--dark-btn);color:var(--white);font-size:12px;display:flex;align-items:center;justify-content:center}

/* contact */
.contact{left:0;top:2053px;width:1200px;height:446px;background:var(--soft)}
.map{left:87px;top:143px;width:494px;height:255px;background:linear-gradient(135deg,#efe9c6 0%,#e6e3d3 45%,#d9e7c4 70%,#f1ecd2 100%)}
.contact-intro{left:624px;top:148px;width:470px;font-size:11px;line-height:20px;color:#777}
.contact h4{font-size:14px;font-weight:500;color:var(--heading)}
.contact .val{font-size:11px;color:var(--muted);margin-top:12px}
.social{display:flex;gap:8px;margin-top:14px}
.social span{width:34px;height:34px;border:1.5px solid #aaa;border-radius:50%;display:flex;align-items:center;justify-content:center}

/* footer */
.site-footer{left:0;top:2499px;width:1200px;height:65px;background:var(--black);color:var(--white);font-size:12px;display:flex;align-items:center;justify-content:center}
</style>
</head>
<body>

<header class="site-header abs">
  <div class="brand abs"><span class="brand-dot"></span><span class="brand-name">Kindred Vantage</span></div>
  <nav class="main-nav">
    <a class="active" href="#" style="left:456px">HOME</a>
    <a href="#" style="left:569px">ABOUT US</a>
    <a href="#" style="left:692px">SERVICES</a>
    <a href="#" style="left:800px">VIDEO</a>
    <a href="#" style="left:897px">BLOG</a>
    <a href="#" style="left:1015px">CONTACT US</a>
  </nav>
  <div class="search-btn abs">
    <svg width="42" height="42" viewBox="0 0 42 42"><circle cx="20" cy="20" r="4.5" fill="none" stroke="#ffd800" stroke-width="2"/><line x1="23.5" y1="23.5" x2="27" y2="27" stroke="#ffd800" stroke-width="2"/></svg>
  </div>
</header>

<section class="hero abs">
  <div class="hero-photo abs" role="img" aria-label="Visitors viewing colourful paintings in a bright gallery"></div>
  <div class="hero-arrow abs" style="left:24px"><svg width="50" height="50" viewBox="0 0 50 50"><polyline points="29,17 21,25 29,33" fill="none" stroke="#999" stroke-width="2.5"/></svg></div>
  <div class="hero-arrow abs" style="left:1121px"><svg width="50" height="50" viewBox="0 0 50 50"><polyline points="21,17 29,25 21,33" fill="none" stroke="#999" stroke-width="2.5"/></svg></div>
</section>

<h2 class="section-title abs center" style="top:607px">OUR SERVICES</h2>
<p class="section-sub abs center" style="top:647px">Sed ut perspiciatis unde omnis iste natus error sit voluptatem accusantium doloremque laudantium, totam</p>

<div class="service abs" style="left:105px;top:699px">
  <div class="service-icon"><div class="inner">
    <svg width="60" height="60" viewBox="0 0 60 60"><path d="M30 30 C22 24 16 19 16 13 C16 9 19 6 23 6 C26 6 28 8 30 10 C32 8 34 6 37 6 C41 6 44 9 44 13 C44 19 38 24 30 30Z" fill="#fff"/><path d="M6 42 L18 36 C22 34 26 35 30 37 L38 37 C41 37 41 41 38 41 L28 41 M38 40 L48 34 C51 32 54 35 51 38 L40 48 C37 50 34 51 30 51 L6 51" fill="none" stroke="#fff" stroke-width="3" stroke-linejoin="round"/></svg>
  </div></div>
  <h3>DIVERSITY</h3>
  <p>Sed ut perspiciatis unde omnis iste natus error sit<br>voluptatem accusantium dolore mque laudantium,<br>beatae vitae dicta sunt explicabo.</p>
</div>

<div class="service abs" style="left:452px;top:699px">
  <div class="service-icon accent"><div class="inner">
    <svg width="64" height="64" viewBox="0 0 64 64"><rect x="26" y="8" width="32" height="22" fill="none" stroke="#fff" stroke-width="3"/><line x1="32" y1="19" x2="50" y2="19" stroke="#fff" stroke-width="3"/><circle cx="15" cy="13" r="5" fill="#fff"/><path d="M9 21 H21 L30 24 L29 27 L21 26 V56 H17 V40 H13 V56 H9Z" fill="#fff"/></svg>
  </div></div>
  <h3>TRAINING</h3>
  <p>Sed ut perspiciatis unde omnis iste natus error sit<br>voluptatem accusantium dolore mque laudantium,<br>beatae vitae dicta sunt explicabo.</p>
</div>

<div class="service abs" style="left:797px;top:699px">
  <div class="service-icon"><div class="inner">
    <svg width="64" height="64" viewBox="0 0 64 64"><rect x="8" y="40" width="5" height="14" fill="#fff"/><rect x="17" y="34" width="5" height="20" fill="#fff"/><rect x="26" y="38" width="5" height="16" fill="#fff"/><rect x="35" y="30" width="5" height="24" fill="#fff"/><rect x="44" y="24" width="5" height="30" fill="#fff"/><polyline points="8,34 20,24 29,30 50,12" fill="none" stroke="#fff" stroke-width="2.5"/><polygon points="44,10 54,8 52,18" fill="#fff"/><line x1="5" y1="57" x2="58" y2="57" stroke="#fff" stroke-width="2"/></svg>
  </div></div>
  <h3>EQUITY</h3>
  <p>Sed ut perspiciatis unde omnis iste natus error sit<br>voluptatem accusantium dolore mque laudantium,<br>beatae vitae dicta sunt explicabo.</p>
</div>

<section class="welcome abs">
  <h2 class="abs">WELCOME KINDRED VANTAGE</h2>
  <div class="tagline abs">SED UT PERSPICIATIS UNDE OMNIS ISTE NATUS ERROR SIT</div>
  <p class="abs" style="top:116px">Sed ut perspiciatis unde omnis iste natus error sit voluptatem accusantium dolore mque laudantium, totam rem aperiam, eaque ipsa quae ab illo inventore veritatis et quasi architecto beatae vitae dicta sunt explicabo.</p>
  <p class="abs" style="top:212px">Nemo enim ipsam voluptatem quia voluptas sit aspernatur aut odit aut fugit, sed quia consequuntur magni dolores eos qui ratione voluptatem sequi nesciunt. Neque porro quisquam est, qui dolorem ipsum quia dolor sit amet, consectetur, adipisci velit, sed quia non numquam</p>
  <div class="btn-outline abs">READ MORE INFO</div>
  <div class="video abs" role="img" aria-label="Video still of a long gallery corridor hung with vivid paintings">
    <div class="play abs"><svg width="66" height="66" viewBox="0 0 66 66"><polygon points="27,20 47,33 27,46" fill="#fff"/></svg></div>
  </div>
</section>

<h2 class="section-title abs center" style="top:1421px">LATEST BLOG</h2>
<p class="section-sub abs center" style="top:1459px">Sed ut perspiciatis unde omnis iste natus error sit voluptatem accusantium doloremque laudantium, totam</p>

<article class="post abs" style="left:87px">
  <div class="post-img" role="img" aria-label="Woman looking at large painted canvases" style="background:linear-gradient(90deg,#6f8a5a,#c9b48a 50%,#8d7a4e)"></div>
  <h3>SED UT PERSPICIATIS UNDE</h3>
  <p>Sed ut perspiciatis unde omnis iste natus error sit voluptatem accusantium doloremque laudantium, totam rem aperiam,eaque beatae vitae dicta sunt explicabo.</p>
  <div class="post-meta"><span><svg width="11" height="11" viewBox="0 0 11 11"><rect x="1" y="2" width="9" height="8" fill="none" stroke="#999"/><line x1="1" y1="4.5" x2="10" y2="4.5" stroke="#999"/></svg>December 29, 2016</span><span><svg width="12" height="11" viewBox="0 0 12 11"><ellipse cx="6" cy="5" rx="5" ry="4" fill="none" stroke="#999"/></svg>05 Comments</span></div>
</article>

<article class="post abs" style="left:436px">
  <div class="post-img" role="img" aria-label="Dancer in a red dress with a burst of coloured paint" style="background:linear-gradient(135deg,#d94b9a 0%,#cfcfcf 40%,#e6e6e6 70%,#9e9e9e 100%)"></div>
  <h3>SED UT PERSPICIATIS UNDE</h3>
  <p>Sed ut perspiciatis unde omnis iste natus error sit voluptatem accusantium doloremque laudantium, totam rem aperiam,eaque beatae vitae dicta sunt explicabo.</p>
  <div class="post-meta"><span><svg width="11" height="11" viewBox="0 0 11 11"><rect x="1" y="2" width="9" height="8" fill="none" stroke="#999"/><line x1="1" y1="4.5" x2="10" y2="4.5" stroke="#999"/></svg>December 29, 2016</span><span><svg width="12" height="11" viewBox="0 0 12 11"><ellipse cx="6" cy="5" rx="5" ry="4" fill="none" stroke="#999"/></svg>05 Comments</span></div>
</article>

<article class="post abs" style="left:783px">
  <div class="post-img" role="img" aria-label="Street canopy of colourful umbrellas" style="background:linear-gradient(180deg,#e2452f 0%,#3f7bc4 45%,#f0b23a 75%,#ddd 100%)"></div>
  <h3>SED UT PERSPICIATIS UNDE</h3>
  <p>Sed ut perspiciatis unde omnis iste natus error sit voluptatem accusantium doloremque laudantium, totam rem aperiam,eaque beatae vitae dicta sunt explicabo.</p>
  <div class="post-meta"><span><svg width="11" height="11" viewBox="0 0 11 11"><rect x="1" y="2" width="9" height="8" fill="none" stroke="#999"/><line x1="1" y1="4.5" x2="10" y2="4.5" stroke="#999"/></svg>December 29, 2016</span><span><svg width="12" height="11" viewBox="0 0 12 11"><ellipse cx="6" cy="5" rx="5" ry="4" fill="none" stroke="#999"/></svg>05 Comments</span></div>
</article>

<section class="newsletter abs">
  <svg class="abs" style="left:135px;top:8px" width="100" height="80" viewBox="0 0 100 80"><path d="M4 30 L50 4 L96 30 V76 H4Z M4 30 L50 56 L96 30" fill="none" stroke="#f0d000" stroke-width="3" opacity=".7"/></svg>
  <div class="label abs">SUBSCRIBE NEWSLETTER :</div>
  <div class="field abs">Enter Your Email Id :</div>
  <div class="submit abs">SUBSCRIBE</div>
</section>

<section class="contact abs">
  <h2 class="section-title abs center" style="top:35px">CONTACT US</h2>
  <p class="section-sub abs center" style="top:82px">Sed ut perspiciatis unde omnis iste natus error sit voluptatem accusantium doloremque laudantium, totam rem</p>
  <div class="map abs" role="img" aria-label="Street map showing the office location"></div>
  <p class="contact-intro abs">Lorem ipsum dolor sit amet, consectetur adipiscing elit, sed do eiusmod tempor inci did unt ut labore et dolore magna aliqua. Ut enim ad minim veniam, quis nostrud exercitatio ullamco laboris nisi ut aliquip ex ea commodo consequat.</p>
  <div class="abs" style="left:624px;top:240px"><h4>ADDRESS</h4><div class="val">Kindred Vantage</div></div>
  <div class="abs" style="left:873px;top:240px"><h4>EMAIL ADDRESS</h4><div class="val">General : hello@kindredvantage.org</div></div>
  <div class="abs" style="left:624px;top:318px"><h4>PHONE</h4><div class="val">Mobile : 555-014-2290</div></div>
  <div class="abs" style="left:873px;top:318px"><h4>FOLLOW US</h4>
    <div class="social"><span></span><span></span><span></span></div>
  </div>
</section>

<footer class="site-footer abs">© Copyright 2016 Kindred Vantage All Rights Reserved</footer>

</body>
</html>
```